Classic Minimalistic Business Card

Design a classic, minimalistic Business Card. Please find inspiration in the attached Classic Minimalistic examples. My information:
Name: Glen Ovamir
Company: Ovamir Capital
Logo: OC
Address: 1470 N Thornwick Rd, Suite 210 | Larkmoor, ST 00000
Phone: 555-555-0192
Email: glenovamir@pvt.insure
Slogan: Building Strength Through Capital

Feel free to leave out any of the information above except my name.

I have selected Double-sided, but I am also open to Single-sided

Target Market(s)

22-70. income greater than 150k/year

Industry/Entity Type

Finance

Contact Information for Business Card

See Project Description

Requirements
Must have
• Ivory or "antiqued" background similar to the reference pictures

```html
<!DOCTYPE html>
<html lang="en">
<head>
<meta charset="utf-8">
<title>Ovamir Capital – Business Card</title>
<link rel="stylesheet" href="https://fonts.googleapis.com/css2?family=Italiana&family=Jost:wght@400&family=Montserrat:wght@600&display=swap">
<style>
  :root {
    --page: #ece8e1;
    --card: #e8dece;
    --card-light: #efe5d5;
    --maroon: #7b0a18;
    --ink: #2a2421;
  }
  * { margin: 0; padding: 0; box-sizing: border-box; }
  html, body { width: 969px; height: 1200px; overflow: hidden; }
  body { background: var(--page); position: relative; font-family: "Montserrat", sans-serif; color: var(--ink); }

  .card {
    position: absolute;
    left: 194px;
    width: 568px;
    height: 340px;
    background: radial-gradient(ellipse at 75% 45%, var(--card-light), var(--card) 70%);
    overflow: hidden;
  }
  .card--front { top: 220px; }
  .card--back { top: 640px; }

  .brand-mark { position: absolute; border-radius: 50%; background: var(--maroon); }
  .card--front .brand-mark { width: 76px; height: 76px; left: 246px; top: 92px; }
  .card--back .brand-mark { width: 52px; height: 52px; left: 56px; top: 46px; }

  .brand-name {
    position: absolute;
    font-family: "Italiana", serif;
    font-weight: 400;
    text-transform: uppercase;
    white-space: nowrap;
    color: var(--ink);
    line-height: 1;
  }
  .brand-tagline {
    position: absolute;
    font-family: "Jost", sans-serif;
    text-transform: uppercase;
    white-space: nowrap;
    color: var(--ink);
    line-height: 1;
  }
  .card--front .brand-name { left: 0; right: 0; text-align: center; top: 208px; font-size: 40px; letter-spacing: 0.01em; }
  .card--front .brand-tagline { left: 0; right: 0; text-align: center; top: 253px; font-size: 12px; letter-spacing: 0.22em; }

  .card--back .brand-name { left: 123px; top: 53px; font-size: 26px; }
  .card--back .brand-tagline { left: 123px; top: 82px; width: 209px; text-align: center; font-size: 8px; letter-spacing: 0.2em; }

  .holder-name {
    position: absolute;
    left: 58px;
    top: 151px;
    font-family: "Italiana", serif;
    font-size: 25px;
    text-transform: uppercase;
    line-height: 1;
    white-space: nowrap;
  }

  .contact-list { position: absolute; left: 59px; top: 194px; list-style: none; }
  .contact-item { display: flex; align-items: center; height: 19px; margin-bottom: 11px; font-size: 13px; white-space: nowrap; }
  .contact-item:nth-child(2) { margin-bottom: 15px; }
  .contact-icon { width: 19px; height: 19px; margin-right: 7px; flex: none; }

  .footer-band { position: absolute; left: 0; right: 4px; bottom: 1px; height: 18px; background: var(--maroon); }
</style>
</head>
<body>

<section class="card card--front">
  <span class="brand-mark"></span>
  <h1 class="brand-name">Ovamir Capital</h1>
  <p class="brand-tagline">Building Strength Through Capital</p>
</section>

<section class="card card--back">
  <span class="brand-mark"></span>
  <h2 class="brand-name">Ovamir Capital</h2>
  <p class="brand-tagline">Building Strength Through Capital</p>

  <p class="holder-name">Glen Ovamir</p>

  <ul class="contact-list">
    <li class="contact-item">
      <svg class="contact-icon" viewBox="0 0 20 20" aria-hidden="true">
        <circle cx="10" cy="10" r="9" fill="none" stroke="#2a2421" stroke-width="1.2"/>
        <path d="M7 5.5l1.6 0 .8 2.2-1 .9a5 5 0 0 0 2.6 2.6l.9-1 2.2.8v1.6a1 1 0 0 1-1.1 1A7.4 7.4 0 0 1 6 6.6a1 1 0 0 1 1-1.1z" fill="#2a2421"/>
      </svg>
      555-555-0192
    </li>
    <li class="contact-item">
      <svg class="contact-icon" viewBox="0 0 20 20" aria-hidden="true">
        <circle cx="10" cy="10" r="9" fill="none" stroke="#2a2421" stroke-width="1.2"/>
        <rect x="5.8" y="7.3" width="8.4" height="5.6" rx="0.6" fill="#2a2421"/>
        <path d="M6 7.6l4 3 4-3" fill="none" stroke="#e8dece" stroke-width="0.8"/>
      </svg>
      glenovamir@pvt.insure
    </li>
    <li class="contact-item">
      <svg class="contact-icon" viewBox="0 0 20 20" aria-hidden="true">
        <circle cx="10" cy="10" r="9" fill="none" stroke="#2a2421" stroke-width="1.2"/>
        <path d="M10 4.6a3.4 3.4 0 0 0-3.4 3.4c0 2.6 3.4 6.4 3.4 6.4s3.4-3.8 3.4-6.4A3.4 3.4 0 0 0 10 4.6z" fill="#2a2421"/>
        <circle cx="10" cy="8" r="1.2" fill="#e8dece"/>
      </svg>
      1470 N Thornwick Rd, Suite 210 | Larkmoor, ST 00000
    </li>
  </ul>

  <div class="footer-band"></div>
</section>

</body>
</html>
```